PLUMBING STICKER AND MAGNET FOR VELMAR PLUMBING GROUP

I need a plumbing sticker and magnet design for marketing our plumbing services. I've attached some examples. Obviously, it must only be the size of a business card. We need similar services listed as on the examples, an QR code, and lic number.
Colour scheme should be blue, grey, black and white. Modern, clean and fresh not as busy as the examples.
The website is www.velmar.com.au
Attached at the logos. Please use random name and contact details at this stage.

```html
<!DOCTYPE html>
<html lang="en">
<head>
<meta charset="utf-8">
<title>Velmar Plumbing Group – Service Card</title>
<link href="https://fonts.googleapis.com/css2?family=Outfit:wght@300;400;500;600;700&display=swap" rel="stylesheet">
<style>
  :root {
    --backdrop: #333333;
    --card: #ffffff;
    --navy: #2a2366;
    --sky: #29abe2;
    --ink: #0d0d0d;
    --text: #1c1c1c;
    --grey: #e4e7eb;
    --grey-line: #9aa3ad;
    --white: #ffffff;
  }
  * { margin: 0; padding: 0; box-sizing: border-box; }
  html, body {
    width: 797px; height: 1200px; overflow: hidden;
    background: var(--backdrop);
    font-family: "Outfit", sans-serif;
  }
  .card {
    position: absolute; left: 71px; top: 27px;
    width: 655px; height: 1146px;
    background: var(--card);
    overflow: hidden;
  }
  .brand { position: absolute; left: 54px; top: 60px; color: var(--navy); font-weight: 600; }
  .brand-name { font-size: 64px; letter-spacing: 14px; line-height: 1; }
  .brand-sub { font-size: 21px; letter-spacing: 10.5px; line-height: 1; margin-top: 14px; }
  .headline { position: absolute; left: 52px; font-weight: 700; line-height: 1; letter-spacing: -1px; }
  .headline-top { top: 212px; font-size: 88px; color: var(--sky); }
  .headline-bottom { top: 304px; font-size: 88px; color: var(--ink); }
  .intro { position: absolute; left: 54px; top: 418px; font-size: 31px; font-weight: 400; color: var(--text); letter-spacing: -0.5px; }
  .services { position: absolute; left: 54px; top: 476px; list-style: none; }
  .services li { position: relative; height: 50px; padding-left: 43px; font-size: 29px; color: var(--text); letter-spacing: -0.3px; }
  .services svg { position: absolute; left: 0; top: 4px; }
  .offer {
    position: absolute; left: 54px; top: 639px; width: 546px; height: 175px;
    background: linear-gradient(150deg, #29abe2 0%, #2c6fb3 40%, #2a2166 80%);
    color: var(--white);
  }
  .offer-title { position: absolute; left: 29px; top: 24px; font-size: 31px; font-weight: 600; letter-spacing: -0.5px; }
  .offer-list { position: absolute; left: 29px; top: 74px; list-style: none; }
  .offer-list li { position: relative; height: 42px; padding-left: 31px; font-size: 28px; font-weight: 300; letter-spacing: -0.5px; }
  .offer-list li::before {
    content: ""; position: absolute; left: 2px; top: 12px;
    border-left: 13px solid var(--white); border-top: 8px solid transparent; border-bottom: 8px solid transparent;
  }
  .badge { position: absolute; left: 406px; top: 522px; }
  .contact { position: absolute; left: 52px; font-size: 58px; font-weight: 600; color: var(--ink); letter-spacing: -2px; line-height: 1; }
  .contact svg { position: absolute; left: 0; }
  .contact span { margin-left: 54px; }
  .contact-phone { top: 842px; }
  .contact-phone svg { top: 8px; }
  .contact-web { top: 910px; }
  .contact-web svg { top: 12px; left: 3px; }
  .divider { position: absolute; left: 54px; top: 994px; width: 547px; height: 2px; background: var(--ink); }
  .footnote { position: absolute; left: 54px; top: 1010px; font-size: 27px; line-height: 40px; color: var(--text); letter-spacing: -0.4px; }
  .licence { font-weight: 600; color: var(--navy); }
  .qr-code {
    position: absolute; left: 497px; top: 1014px; width: 104px; height: 104px;
    background: var(--grey); border: 2px solid var(--grey-line);
  }
</style>
</head>
<body>
  <main class="card">
    <div class="brand">
      <div class="brand-name">VELMAR</div>
      <div class="brand-sub">PLUMBING GROUP</div>
    </div>

    <h1 class="headline headline-top">PLUMBING</h1>
    <h2 class="headline headline-bottom">SERVICES</h2>

    <p class="intro">All Plumbing Services</p>
    <ul class="services">
      <li><svg width="28" height="26" viewBox="0 0 28 26"><path d="M2 14 L10 23 L26 2" fill="none" stroke="#29abe2" stroke-width="3.5" stroke-linecap="round" stroke-linejoin="round"/></svg>Blocked Drains</li>
      <li><svg width="28" height="26" viewBox="0 0 28 26"><path d="M2 14 L10 23 L26 2" fill="none" stroke="#29abe2" stroke-width="3.5" stroke-linecap="round" stroke-linejoin="round"/></svg>Hot Water Systems</li>
      <li><svg width="28" height="26" viewBox="0 0 28 26"><path d="M2 14 L10 23 L26 2" fill="none" stroke="#29abe2" stroke-width="3.5" stroke-linecap="round" stroke-linejoin="round"/></svg>Gas fitting</li>
    </ul>

    <section class="offer">
      <h3 class="offer-title">We Offer</h3>
      <ul class="offer-list">
        <li>24/7 Days/week</li>
        <li>365 Days/year service</li>
      </ul>
    </section>

    <svg class="badge" width="204" height="204" viewBox="0 0 204 204" aria-hidden="true">
      <defs>
        <linearGradient id="badgeFill" x1="0" y1="0" x2="1" y2="1">
          <stop offset="0" stop-color="#1d4f8f"/>
          <stop offset="0.6" stop-color="#00aeef"/>
        </linearGradient>
      </defs>
      <circle cx="102" cy="102" r="102" fill="#ffffff"/>
      <circle cx="102" cy="102" r="92" fill="url(#badgeFill)"/>
    </svg>

    <div class="contact contact-phone">
      <svg width="40" height="40" viewBox="0 0 24 24"><path fill="#29abe2" d="M6.6 10.8c1.4 2.8 3.8 5.1 6.6 6.6l2.2-2.2c.3-.3.7-.4 1-.2 1.1.4 2.3.6 3.6.6.6 0 1 .4 1 1V20c0 .6-.4 1-1 1C10.6 21 3 13.4 3 4c0-.6.4-1 1-1h3.5c.6 0 1 .4 1 1 0 1.3.2 2.5.6 3.6.1.3 0 .7-.2 1L6.6 10.8z"/></svg>
      <span>1800 555 214</span>
    </div>
    <div class="contact contact-web">
      <svg width="28" height="38" viewBox="0 0 28 38"><path fill="#29abe2" d="M0 0 L0 28 L7 22 L12 36 L18 33 L13 20 L24 20 Z"/></svg>
      <span>velmar.com.au</span>
    </div>

    <div class="divider"></div>
    <p class="footnote">We offer Pension, Senior Discounts,<br>NOVA, Credipay, VIRO<br><span class="licence">Lic. No. 284615</span></p>
    <div class="qr-code" role="img" aria-label="QR code linking to velmar.com.au"></div>
  </main>
</body>
</html>
```